Kiswa Design

We need a flyer design for a product that we are a selling, a sacred Islamic cloth called a Kiswah, which is draped around the holy Kaaba in mecca every year.

The details we would like on the flyer are as follows:

Rare Kiswah of the holy Kaaba for sale (fitted in 1977 and 1982 vintage). For sale:

1) whole piece 15 meters x 2.60 meters : £60,000
2) 8 meters x 2.60 meters : £31,200
3) 4 meters x 2.60 meters : £15,600
4) 1 meter : £1500

(insert a high quality picture of holy Kaaba here, then underneath the picture, write the following:) "The Kaaba is covered by an expensive black cloth which is known as 'Kiswah' which is produced and changed every year"

(insert picture of our product here,i.e. use the document named MAIN IMAGE then underneath this picture write the following:) "Silk lampas weave Kiswah, woven silk on a black satin ground with Quranic calligraphy, the zig-zag bands of inscription alternate with the Shahadah and the inscription, 'God, exalted be His Glory!"

insert another picture of kiswah which i provided anywhere you like

(somewhere on flyer write the following) please note a percentage of sales will go towards Sadaqah for our Muslim brothers and sisters in need around the world

(somewhere on flyer write the following) Harwell's international auction house authenticity document also available to prove the Kiswah is genuine.

100% genuine

contact us today! deals this good don't last forever.

email: clothoffer@mailverno.com

Please use the images that I have attached on the flyer accordingly. Also feel free to be as creative as possible I want it to attract a lot of attention but also look professional so you may add some things to improve the look of the flyer.

note: the product being sold is on the pictures I've provided, in particular, i want file 2 "main image" in a large size on the flyer!

thank you! and happy holidays

Target Market(s)

Muslims and Islamic collectors

Industry/Entity Type

House

Requirements
Must have
• the dimensions of the flyer is :
• A5 horizontal or vertical
• (210 x 148 mm)
• must have colors! up to you what colors to choose!

```html
<!DOCTYPE html>
<html lang="en">
<head>
<meta charset="utf-8">
<title>Rare Kiswah of the Holy Kaaba for Sale</title>
<link href="https://fonts.googleapis.com/css2?family=Roboto+Condensed:ital,wght@0,400;0,700;1,700&family=Oswald:wght@600&family=Arimo:ital,wght@0,400;0,700;1,400&display=swap" rel="stylesheet">
<style>
  :root {
    --gold: #dcab3d;
    --ink: #0b0b0b;
    --paper: #ffffff;
    --white: #ffffff;
    --fog: #d8d8d8;
    --slate: rgba(72, 72, 72, 0.85);
  }
  * { margin: 0; padding: 0; box-sizing: border-box; }
  html, body { width: 897px; height: 1200px; overflow: hidden; background: var(--paper); }
  .canvas { position: relative; width: 897px; height: 1200px; }
  .flyer { position: absolute; left: 111px; top: 122px; width: 675px; height: 956px; overflow: hidden;
    box-shadow: 0 20px 40px rgba(0,0,0,0.12); }

  .fabric-backdrop {
    position: absolute; left: 0; top: 240px; width: 288px; height: 716px;
    background: linear-gradient(180deg, #e6e6e6 0%, #c6c6c6 30%, #9a9a9a 58%, #5a5a5a 100%);
  }
  .title-banner { position: absolute; left: 0; top: 0; width: 288px; height: 285px; }
  .title-banner svg { position: absolute; inset: 0; }
  .title { position: absolute; left: 39px; top: 38px; width: 212px; color: var(--ink);
    font-family: "Roboto Condensed", "Arial Narrow", sans-serif; }
  .title > span { display: block; white-space: nowrap; }
  .title-lead { font-family: "Oswald", sans-serif; font-weight: 600; font-size: 35px; line-height: 36px; letter-spacing: 0.6px; }
  .title-sub { font-weight: 400; font-size: 25.5px; line-height: 24px; letter-spacing: -0.2px; }
  .title > .title-for { display: flex; align-items: center; gap: 8px; margin-top: 2px; font-size: 11px; line-height: 12px; }
  .title-for::before, .title-for::after { content: ""; flex: 1; height: 1px; background: var(--ink); }
  .title-sale { font-family: "Oswald", sans-serif; font-weight: 600; font-size: 108px; line-height: 86px; letter-spacing: 2px; margin-left: -2px; }
  .title-vintage { font-weight: 700; font-size: 13px; line-height: 14px; margin-top: 8px; }

  .kiswah-intro {
    position: absolute; left: 30px; top: 292px; width: 236px;
    font-family: "Roboto Condensed", "Arial Narrow", sans-serif; font-weight: 700;
    font-size: 17.5px; line-height: 21px; color: #1c1c1c; text-align: center; letter-spacing: 0.3px;
    text-shadow: 0 0 3px rgba(255,255,255,0.8);
  }
  .kiswah-intro .term { display: block; text-align: left; font-style: italic; }

  .weave-caption {
    position: absolute; left: 30px; top: 482px; width: 229px; padding: 4px 4px 6px;
    background: var(--slate); color: var(--white);
    font-family: "Roboto Condensed", "Arial Narrow", sans-serif; font-size: 16.5px; line-height: 23.5px;
  }
  .weave-caption span { display: block; text-align: justify; text-align-last: justify; white-space: nowrap; }
  .weave-caption span:last-child { text-align-last: left; }

  .sadaqah-note {
    position: absolute; left: 37px; top: 848px; width: 222px;
    font-family: "Roboto Condensed", "Arial Narrow", sans-serif; font-size: 14.5px; line-height: 17.5px; color: var(--fog);
  }

  .kaaba-photo { position: absolute; left: 288px; top: 0; width: 387px; height: 463px;
    background: linear-gradient(180deg, #3a3a3a 0%, #1c1c1c 35%, #121212 100%); }
  .cloth-folded { position: absolute; left: 288px; top: 463px; width: 146px; height: 195px;
    background: linear-gradient(160deg, #8a8a8a 0%, #3c3c3c 45%, #262626 100%); }
  .cloth-detail { position: absolute; left: 434px; top: 463px; width: 241px; height: 195px;
    background: linear-gradient(180deg, #2c2c2c 0%, #1f1f1f 100%);
    border-left: 4px solid #1a1a1a; }

  .pricing { position: absolute; left: 288px; top: 658px; width: 387px; height: 178px; background: var(--ink); padding: 20px 10px 0 9px; }
  .authenticity { font-family: "Roboto Condensed", "Arial Narrow", sans-serif; font-weight: 700; font-size: 13px; line-height: 18px; color: var(--gold); white-space: nowrap; }
  .authenticity .wide { letter-spacing: 1.5px; }
  .price-list { list-style: none; margin-top: 12px; font-family: "Arimo", Helvetica, sans-serif; font-size: 14.5px; line-height: 19px; color: var(--white); }

  .contact { position: absolute; left: 288px; top: 836px; width: 387px; height: 120px; background: var(--gold); padding: 26px 0 0 35px;
    font-family: "Arimo", Helvetica, sans-serif; font-size: 18.5px; line-height: 24.5px; color: var(--ink);
    -webkit-text-stroke: 0.35px var(--ink); }
  .contact em { font-style: italic; }
</style>
</head>
<body>
<div class="canvas">
  <article class="flyer">
    <div class="fabric-backdrop" role="img" aria-label="Close-up of grey kiswah cloth with woven calligraphy"></div>

    <header class="title-banner">
      <svg width="288" height="285" viewBox="0 0 288 285" aria-hidden="true">
        <polygon points="0,0 288,0 288,242 144,284 0,242" fill="var(--gold)"/>
      </svg>
      <h1 class="title">
        <span class="title-lead">RARE KISWAH</span>
        <span class="title-sub">OF THE HOLY KAABA</span>
        <span class="title-for">FOR</span>
        <span class="title-sale">SALE</span>
        <span class="title-vintage">(FITTED IN 1977 AND 1982 VINTAGE)</span>
      </h1>
    </header>

    <p class="kiswah-intro">THE KAABA IS COVERED BY<br>AN EXPENSIVE BLACK CLOTH<br>WHICH IS KNOWN AS<span class="term">'KISWAH'</span>WHICH IS PRODUCED AND<br>CHANGED EVERY YEAR"</p>

    <p class="weave-caption">
      <span>Silk lampas weave Kiswah,</span>
      <span>woven silk on a black satin</span>
      <span>ground with Quranic</span>
      <span>calligraphy, the zig-zag bands</span>
      <span>of inscription alternate with the</span>
      <span>Shahadah and the inscription,</span>
      <span>'God, exalted be His Glory!"</span>
    </p>

    <p class="sadaqah-note">Please note a percentage of sales<br>will go towards sadaqah for our<br>muslim brothers and sisters in need<br>around the world.</p>

    <div class="kaaba-photo" role="img" aria-label="The Holy Kaaba draped in its black kiswah with gold embroidered band and door curtain"></div>
    <div class="cloth-folded" role="img" aria-label="Folded black kiswah cloth"></div>
    <div class="cloth-detail" role="img" aria-label="Black kiswah satin with woven zig-zag calligraphy and gold edge"></div>

    <section class="pricing">
      <p class="authenticity"><span class="wide">Harwell's international auction house authenticity</span><br>document also available to prove the Kiswah is genuine.</p>
      <ol class="price-list">
        <li>1) whole piece 15 meters x 2.60 meters : £60,000</li>
        <li>2) 8 meters x 2.60 meters : £31,200</li>
        <li>3) 4 meters x 2.60 meters : £15,600</li>
        <li>4) 1 meter : £1500</li>
      </ol>
    </section>

    <footer class="contact">
      <p>100% genuine! <em>contact us today!</em></p>
      <p>Deals this good don't last forever.</p>
      <p>email: <em>clothoffer@mailverno.com</em></p>
    </footer>
  </article>
</div>
</body>
</html>
```